CD-/Plattencover für eine Tonträgerfirma
Zielgruppe
Wir sind eine Tonträgerfirma und bewegen uns im Low-Budget-Segment.
Aufgabenstellung
'Harbor Lanterns'
Wir benötigen nicht das komplette Artwork, sondern ein Frontcover
(121 x 120 mm + 20 mm Beschnitt) wg. etwaiger Verschiebung der Positionierung.
Fertigstellung (Aufziehen des Inlays und Labels) erfolgt später bei uns im Hause.
Wir benötigen später eine offene psd-Datei mit allen Ebenen.
Wichtig: Schriften nicht gerastert ggfs. Schrift mitliefern.
Was wir uns vorstellen:
- Entsprechend der Musik Bild
- Da es ein 2-CD-Set ist, sollte '2 CDs' auch gut auf dem Cover ersichtlich sein
- Folgende Titel sollten auf dem Cover genannt werden
Rowan Lad
Hills of Fern
Gentle Harrow
- Bildmaterial sollte bei pixelbarn, bildora oder n-pics ausgesucht werden,
das Bildmaterial wird dann später auch von uns dort eingekauft
- keine Künstlerfotos
- vorzugsweise nur 1 Bild pro Layout, max. 2 Bilder
Wir freuen uns und sind sehr gespannt auf eure Vorschläge,
bei Fragen gerne mailen

```html
<!DOCTYPE html>
<html lang="en">
<head>
<meta charset="utf-8">
<title>Harbor Lanterns – 2-CD Set Front Cover</title>
<link rel="stylesheet" href="https://fonts.googleapis.com/css2?family=Uncial+Antiqua&family=Cormorant+Garamond:ital,wght@1,600&family=Montserrat:wght@700&display=swap">
<style>
  :root {
    --green-deep: #2f7f2c;
    --green-base: #3f9a3a;
    --green-light: #55b04a;
    --green-line: #84c873;
    --green-ring: #4da544;
    --green-ring-dark: #32802f;
    --badge-fill: #2b6e29;
    --track-text: #e4f2d6;
    --white: #ffffff;
    --shadow: rgba(10, 40, 10, 0.65);
  }
  html, body {
    margin: 0;
    padding: 0;
    overflow: hidden;
    background: var(--green-base);
  }
  .cover {
    position: relative;
    width: 1200px;
    height: 1194px;
    overflow: hidden;
    background: radial-gradient(circle at 50% 47%, var(--green-light) 0%, var(--green-base) 55%, var(--green-deep) 100%);
    font-family: "Montserrat", sans-serif;
  }
  .cover__frame {
    position: absolute;
    inset: 0;
  }
  .cover__title {
    position: absolute;
    left: 0;
    top: 0;
    width: 1200px;
    height: 1194px;
    pointer-events: none;
  }
  .title__main {
    position: absolute;
    left: 150px;
    top: 500px;
    width: 780px;
    text-align: center;
    margin: 0;
    font-family: "Uncial Antiqua", serif;
    font-weight: 400;
    font-size: 168px;
    line-height: 1;
    color: var(--white);
    text-transform: lowercase;
    text-shadow: 4px 6px 10px var(--shadow);
  }
  .title__sub {
    position: absolute;
    right: 250px;
    top: 700px;
    margin: 0;
    font-family: "Cormorant Garamond", serif;
    font-style: italic;
    font-weight: 600;
    font-size: 118px;
    line-height: 1;
    color: var(--white);
    text-shadow: 3px 5px 8px var(--shadow);
  }
  .badge {
    position: absolute;
    left: 978px;
    top: 92px;
    width: 104px;
    height: 104px;
    border-radius: 50%;
    background: var(--badge-fill);
    box-shadow: 0 0 0 6px var(--green-light), 0 0 0 9px var(--green-deep);
    display: flex;
    flex-direction: column;
    align-items: center;
    justify-content: center;
    color: var(--white);
    font-weight: 700;
    line-height: 1.05;
  }
  .badge__count { font-size: 28px; }
  .badge__label { font-size: 28px; }
  .tracklist {
    position: absolute;
    left: 0;
    width: 1200px;
    top: 1092px;
    margin: 0;
    display: flex;
    align-items: center;
    justify-content: center;
    gap: 16px;
  }
  .tracklist__rule {
    width: 44px;
    height: 4px;
    background: var(--green-line);
  }
  .tracklist__titles {
    font-size: 19px;
    font-weight: 700;
    letter-spacing: 3px;
    line-height: 1;
    color: var(--track-text);
    text-transform: uppercase;
    white-space: nowrap;
  }
  .tracklist__sep { margin: 0 8px; }
</style>
</head>
<body>
<main class="cover">
  <svg class="cover__frame" width="1200" height="1194" viewBox="0 0 1200 1194">
    <g stroke="var(--green-line)" stroke-width="4" fill="none">
      <line x1="210" y1="82" x2="990" y2="82"/>
      <line x1="92" y1="230" x2="92" y2="960"/>
      <line x1="1108" y1="230" x2="1108" y2="960"/>
    </g>
    <circle class="ring-pattern" cx="600" cy="555" r="470" fill="var(--green-ring)" role="img" aria-label="Ring of interlaced knotwork ornaments around the central image"/>
    <circle cx="600" cy="555" r="420" fill="var(--green-base)"/>
    <circle cx="600" cy="555" r="400" fill="var(--green-ring)" role="img" aria-label="Inner ring of knotwork ornaments"/>
    <circle cx="600" cy="555" r="340" fill="var(--green-ring-dark)"/>
    <defs>
      <linearGradient id="sceneTone" x1="0" y1="0" x2="0" y2="1">
        <stop offset="0" stop-color="#3b8f36"/>
        <stop offset="0.35" stop-color="#4e7a36"/>
        <stop offset="0.7" stop-color="#1f4d2a"/>
        <stop offset="1" stop-color="#2f7a2c"/>
      </linearGradient>
    </defs>
    <circle class="scene" cx="600" cy="555" r="325" fill="url(#sceneTone)" role="img" aria-label="Photograph of green coastal cliffs rising above a dark sea"/>
    <circle cx="600" cy="555" r="325" fill="none" stroke="var(--green-light)" stroke-width="6"/>
  </svg>

  <div class="cover__title">
    <h1 class="title__main">harbor</h1>
    <p class="title__sub">Lanterns</p>
  </div>

  <div class="badge">
    <span class="badge__count">2-CD</span>
    <span class="badge__label">Set</span>
  </div>

  <div class="tracklist">
    <span class="tracklist__rule"></span>
    <p class="tracklist__titles" style="margin:0">Rowan Lad<span class="tracklist__sep">•</span>Hills of Fern<span class="tracklist__sep">•</span>Gentle Harrow</p>
    <span class="tracklist__rule"></span>
  </div>
</main>
</body>
</html>
```